Selka Marven Photography Business Card

I need a new business card/ possibly design to use for other marking materials ... I have included my logo below in a few different colors, but can also provide the logo in additional colors and sizes. I would love a card the expresses clean, simple and classy.

Target Market(s)

Portrait photography clients, child photography clients

Industry/Entity Type

Photographer

Contact Information for Business Card

Selka Marven Photography, Corvell Falls MA, www.selkamarvenphotography-demo.com
T. 555-203-1946 E. selkamarvenphoto@mailbox-demo.com

Colors
33b8a4
eea4c8
5c5c5c

Requirements
Must have
• I would like to include my logo on card.
Nice to have
• I also like the color brown as well as the choices below. I would like a simple, elegant card, something classy.

```html
<!DOCTYPE html>
<html lang="en">
<head>
<meta charset="utf-8">
<title>Selka Marven Photography – Business Card</title>
<link rel="stylesheet" href="https://fonts.googleapis.com/css2?family=Josefin+Sans:wght@300;400;600;700&display=swap">
<style>
  :root {
    --canvas: #ececec;
    --card-white: #ffffff;
    --stripe-tone: linear-gradient(135deg, #6f6f6f 0%, #8a8a8a 50%, #6f6f6f 100%);
    --ink: #1e1e1e;
    --ink-soft: #8c8c8c;
    --rule: #9a9a9a;
    --icon: #7a7a7a;
    --shadow: 0 14px 30px rgba(0,0,0,0.18);
  }
  * { box-sizing: border-box; margin: 0; padding: 0; }
  html, body { width: 1200px; height: 750px; overflow: hidden; }
  body {
    background: var(--canvas);
    font-family: "Josefin Sans", sans-serif;
    color: var(--ink);
    position: relative;
  }
  .card {
    position: absolute;
    width: 560px;
    height: 320px;
    border-radius: 28px;
    overflow: hidden;
    box-shadow: var(--shadow);
  }
  .card-front { left: 50px; top: 60px; }
  .card-back { left: 590px; top: 370px; }
  .stripe-field {
    position: absolute;
    inset: 0;
    background: var(--stripe-tone);
  }
  .front-panel {
    position: absolute;
    left: 124px; top: 34px;
    right: 0; height: 196px;
    background: var(--card-white);
    display: flex;
    align-items: center;
    justify-content: center;
  }
  .brand-name {
    font-weight: 300;
    font-size: 24px;
    letter-spacing: 0.14em;
    color: var(--ink);
    text-transform: uppercase;
    text-align: center;
    line-height: 1.5;
  }
  .back-panel {
    position: absolute;
    left: 0; top: 88px;
    width: 400px; height: 198px;
    background: var(--card-white);
  }
  .icon-column {
    position: absolute;
    left: 0; top: 0; bottom: 0;
    width: 52px;
    border-right: 1px solid var(--rule);
  }
  .contact-row {
    position: absolute;
    left: 0; right: 0;
    display: flex;
    align-items: center;
    border-top: 1px solid var(--rule);
  }
  .contact-row:first-child { border-top: none; }
  .row-icon {
    width: 52px;
    display: flex;
    justify-content: center;
    flex-shrink: 0;
  }
  .row-icon svg { width: 16px; height: 16px; fill: var(--icon); }
  .row-text {
    padding-left: 14px;
    font-size: 11px;
    font-weight: 600;
    letter-spacing: 0.05em;
    text-transform: uppercase;
    line-height: 1.5;
    white-space: nowrap;
  }
  .row-name { top: 0; height: 62px; }
  .row-phone { top: 62px; height: 40px; }
  .row-web { top: 102px; height: 52px; }
  .row-place { top: 154px; height: 44px; }
  .person-name {
    font-size: 21px;
    font-weight: 700;
    letter-spacing: 0.06em;
    line-height: 1.05;
  }
  .person-role {
    font-size: 11px;
    font-weight: 400;
    letter-spacing: 0.1em;
    color: var(--ink-soft);
  }
</style>
</head>
<body>
  <section class="card card-front" aria-label="Card front">
    <div class="stripe-field" role="img" aria-label="Black and white diagonal stripe pattern"></div>
    <div class="front-panel">
      <p class="brand-name">Selka Marven<br>Photography</p>
    </div>
  </section>

  <section class="card card-back" aria-label="Card back">
    <div class="stripe-field" role="img" aria-label="Black and white diagonal stripe pattern"></div>
    <div class="back-panel">
      <div class="icon-column"></div>

      <div class="contact-row row-name">
        <span class="row-icon">
          <svg viewBox="0 0 16 16"><circle cx="8" cy="5" r="3.2"/><path d="M2 15c0-3.6 2.7-5.6 6-5.6s6 2 6 5.6z"/></svg>
        </span>
        <div class="row-text">
          <div class="person-name">Selka Marven</div>
          <div class="person-role">Photographer</div>
        </div>
      </div>

      <div class="contact-row row-phone">
        <span class="row-icon">
          <svg viewBox="0 0 16 16"><path d="M4.2 1.5l2 3-1.4 1.4c.8 1.8 2.3 3.3 4.1 4.1l1.4-1.4 3 2-1 2.5c-5.5.3-10.2-4.4-9.9-9.9z"/></svg>
        </span>
        <div class="row-text">555-203-1946</div>
      </div>

      <div class="contact-row row-web">
        <span class="row-icon">
          <svg viewBox="0 0 16 16"><path d="M1 2h14v9H1zM2.3 3.3v6.4h11.4V3.3zM6 12h4l.6 2H5.4z"/></svg>
        </span>
        <div class="row-text">selkamarvenphoto@mailbox-demo.com<br>www.selkamarvenphotography-demo.com</div>
      </div>

      <div class="contact-row row-place">
        <span class="row-icon">
          <svg viewBox="0 0 16 16"><path d="M8 1a5 5 0 0 0-5 5c0 3.6 5 9 5 9s5-5.4 5-9a5 5 0 0 0-5-5zm0 7a2 2 0 1 1 0-4 2 2 0 0 1 0 4z"/></svg>
        </span>
        <div class="row-text">Corvell Falls MA</div>
      </div>
    </div>
  </section>
</body>
</html>
```